Designs for a Barrister's chambers

Design stationery (including business card and letterhead) for a barrister's chambers -- similar to a law firm, using the enclosed logo. The current designs are not fit for purpose.

```html
<!DOCTYPE html>
<html lang="en">
<head>
<meta charset="utf-8">
<title>Crownhall Chambers – Business Card</title>
<link href="https://fonts.googleapis.com/css2?family=Montserrat:wght@400;700&family=Roboto+Condensed:wght@300;400&display=swap" rel="stylesheet">
<style>
  :root {
    --backdrop: #c9c9c9;
    --paper: #ffffff;
    --teal: #0096b4;
    --navy: #0d1b33;
    --ink: #4a4a4a;
    --card-back: #021a35;
    --pattern-blue: #1466c8;
    --pattern-dark: #02060c;
  }
  * { margin: 0; padding: 0; box-sizing: border-box; }
  html, body { width: 1200px; height: 1200px; overflow: hidden; }
  body { background: var(--backdrop); position: relative; }

  .card { position: absolute; left: 262px; width: 686px; height: 392px; }
  .card-front { top: 165px; background: var(--paper); }
  .card-back { top: 653px; background: var(--card-back); }

  .name-band {
    position: absolute; left: 0; top: 49px; width: 395px; height: 66px;
    background: var(--teal); color: #fff;
    font-family: "Montserrat", sans-serif; padding: 12px 0 0 40px;
  }
  .name-band .person { font-weight: 700; font-size: 24px; line-height: 1.1; display: block; }
  .name-band .role { font-weight: 400; font-size: 15.5px; letter-spacing: 0.5px; display: block; margin-top: 1px; }

  .brand-square {
    position: absolute; left: 397px; top: 50px; width: 64px; height: 64px;
    background: var(--teal);
  }
  .brand-name {
    position: absolute; left: 474px; top: 48px;
    font-family: "Montserrat", sans-serif; font-weight: 700; font-size: 29px;
    line-height: 36px; color: var(--navy); letter-spacing: -0.5px;
  }

  .contact-list {
    position: absolute; left: 37px; top: 283px; list-style: none;
    font-family: "Roboto Condensed", sans-serif; font-weight: 300; font-size: 15.5px;
    color: var(--ink);
  }
  .contact-list li { display: flex; align-items: center; height: 19.5px; }
  .contact-list svg { width: 13px; height: 13px; margin-right: 9px; fill: var(--teal); flex: none; }

  .address {
    position: absolute; right: 40px; top: 300px; text-align: right;
    font-family: "Roboto Condensed", sans-serif; font-weight: 300; font-size: 15.5px;
    line-height: 20.5px; color: var(--ink);
  }

  .pattern-field {
    position: absolute; left: 8px; top: 9px; right: 9px; bottom: 7px;
    background: linear-gradient(90deg, var(--pattern-blue) 0%, #0a3a7a 40%, #04152b 65%, var(--pattern-dark) 100%);
    opacity: 0.85;
  }
</style>
</head>
<body>
  <section class="card card-front">
    <div class="name-band">
      <span class="person">Marcus Hollowell</span>
      <span class="role">Barrister</span>
    </div>
    <div class="brand-square"></div>
    <div class="brand-name">Crownhall<br>Chambers</div>

    <ul class="contact-list">
      <li><svg viewBox="0 0 16 16"><path d="M3.5 1 6 3.8 4.8 5.6c.9 2 2.6 3.7 4.6 4.6l1.8-1.2L14 11.5l-1.5 2.7C7 14 2 9 1.8 3.5Z"/></svg>0203 555 0141</li>
      <li><svg viewBox="0 0 16 16"><path d="M4 1h8v14H4Zm1.5 1.5v9h5v-9ZM7 12.5v1h2v-1Z"/></svg>07700 900 412</li>
      <li><svg viewBox="0 0 16 16"><path d="M4 1h8v4H4ZM1 6h14v6h-3v3H4v-3H1Zm4.5 4v3.5h5V10Z"/></svg>0203 555 0142</li>
      <li><svg viewBox="0 0 16 16"><path d="M1 3h14v1.5L8 9 1 4.5Zm0 3 7 4.5L15 6v7H1Z"/></svg>marcus.hollowell@crownhallchambers.com</li>
    </ul>

    <div class="address">
      42 Carter Lane<br>
      London EC4V 5AB<br>
      www.crownhallchambers.com
    </div>
  </section>

  <section class="card card-back">
    <div class="pattern-field" role="img" aria-label="Repeating grid of the chambers mark fading from bright blue on the left to black on the right"></div>
  </section>
</body>
</html>
```